Energieberatung sucht Corporate Design
Zielgruppe
Ich führe Energieberatungen für Immobilieneigentümer durch, erstelle Sanierungsvorschläge sowie Förderanträge. Für Verkäufer und Vermieter fertige ich Energieausweise an, um die energetisch Qualität des Gebäudes darzustellen.
Energieberatung soll für die Kunden ein Wegweiser für modernes, klimaneutrales und kostengünstiges Wohnen sein.
Meine Zielgruppe sind Immobilieneigentümer, Verkäufer und Vermieter von Immobilien sowie Käufer von Immobilien.
Aufgabenstellung
Ich suche ein hochwertiges Design, welches modern und zeitlos ist, aber auch die energetische Komponente berücksichtigt. Mit dem Design soll das verstaubte Image der Energieberatung abgelegt werden. Die Kunden sollen damit zukunftsorientiertes, modernes Wohnen, Wohnqualität und Kostenersparnis verbinden.

```html
<!DOCTYPE html>
<html lang="de">
<head>
<meta charset="utf-8">
<title>Energieberatung Lennart Vossberg – Geschäftsausstattung</title>
<link href="https://fonts.googleapis.com/css2?family=Exo+2:wght@400;500&family=PT+Sans:wght@400;700&display=swap" rel="stylesheet">
<style>
:root{
  --backdrop:#c9ccd1;
  --paper:#ffffff;
  --paper-grey:#e8e8e6;
  --teal:#137b98;
  --lime:#bdbd0e;
  --ink:#1f1f1f;
  --text-grey:#575757;
  --rule:#c8c8c8;
}
*{box-sizing:border-box;margin:0;padding:0}
html,body{width:999px;height:1200px;overflow:hidden;background:var(--backdrop)}
body{font-family:"PT Sans",Arial,sans-serif;color:var(--ink)}
.canvas{position:relative;width:999px;height:1200px;overflow:hidden;background:var(--backdrop)}
.sheet{position:absolute;background:var(--paper);box-shadow:2px 4px 8px rgba(0,0,0,.22)}

/* wordmark */
.wordmark{display:flex;align-items:center;gap:8px;font-family:"Exo 2",Arial,sans-serif;font-weight:400;line-height:1.05;color:var(--teal)}
.wordmark .mark-square{flex:none;background:var(--lime)}
.wordmark .name span{display:block}

/* presentation card */
.logo-card{left:362px;top:28px;width:582px;height:264px;display:flex;align-items:center;justify-content:center}
.logo-card .wordmark{font-size:24px}
.logo-card .mark-square{width:22px;height:22px}

/* business card front */
.card-front{left:56px;top:340px;width:235px;height:153px;overflow:hidden}
.card-front .wordmark{position:absolute;left:62px;top:26px;font-size:10px;gap:5px}
.card-front .mark-square{width:9px;height:9px}
.card-front .holder{position:absolute;left:16px;top:73px;font-size:6.8px;line-height:1.5}
.card-front .holder b{color:var(--teal)}
.card-front .holder span{color:var(--text-grey)}
.card-front .address{position:absolute;left:16px;top:117px;font-size:6.6px;line-height:1.6;color:var(--ink)}
.card-front .divider{position:absolute;left:118px;top:98px;width:1px;height:47px;background:var(--teal)}
.card-front .contact{position:absolute;left:128px;top:100px;font-size:6.4px;line-height:1.6;color:var(--teal)}
.contact li{list-style:none;display:flex;align-items:center;gap:4px}
.contact svg{width:6px;height:6px;flex:none}
.card-front .base-band{position:absolute;left:0;bottom:0;width:100%;height:7px;background:var(--lime);clip-path:polygon(3% 0,97% 0,100% 100%,0 100%)}

/* business card back */
.card-back{left:56px;top:508px;width:235px;height:152px;background:var(--teal);display:flex;flex-direction:column;align-items:center;justify-content:center;gap:16px}
.card-back .wordmark{color:var(--lime);font-size:12px}
.card-back .mark-square{width:11px;height:11px;background:var(--lime)}
.card-back .url{color:#fff;font-weight:700;font-size:7px}

/* variant cards */
.variant{left:55px;width:235px;height:152px;display:flex;align-items:center;justify-content:center}
.variant .wordmark{font-size:13px}
.variant .mark-square{width:12px;height:12px}
.variant-grey{top:697px;background:var(--paper-grey)}
.variant-mono{top:866px}
.variant-mono .wordmark{color:var(--ink)}
.variant-mono .mark-square{background:var(--ink)}

/* letterhead */
.letterhead{left:364px;top:340px;width:580px;height:820px}
.letterhead .wordmark{position:absolute;left:210px;top:40px;font-size:14px}
.letterhead .mark-square{width:13px;height:13px}
.fold-mark{position:absolute;left:0;width:20px;height:1px;background:var(--rule)}
.sender-line{position:absolute;left:59px;top:123px;font-size:6.6px;color:var(--teal)}
.recipient{position:absolute;left:59px;top:146px;font-size:10.7px;line-height:14px}
.letter-body{position:absolute;left:59px;top:250px;width:470px;font-size:10.7px;line-height:14px}
.letter-body p{margin-bottom:14px}
.letter-body .subject{margin-bottom:23px}
.letter-body .salutation{margin-bottom:14px}
.letter-footer{position:absolute;left:59px;top:766px;display:flex;font-size:6.4px;line-height:1.75;color:var(--text-grey)}
.letter-footer section{margin-right:26px}
.letter-footer h4{color:var(--teal);font-weight:700;font-size:6.4px}
.letter-footer .contact{color:var(--text-grey)}
.letter-footer .contact svg{width:5.5px;height:5.5px}
.letterhead .base-band{position:absolute;left:0;bottom:0;width:100%;height:8px;background:var(--teal);clip-path:polygon(1% 0,99% 0,100% 100%,0 100%)}
</style>
</head>
<body>
<div class="canvas">

  <div class="sheet logo-card">
    <div class="wordmark"><i class="mark-square"></i><div class="name"><span>Energieberatung</span><span>Lennart Vossberg</span></div></div>
  </div>

  <div class="sheet card-front">
    <div class="wordmark"><i class="mark-square"></i><div class="name"><span>Energieberatung</span><span>Lennart Vossberg</span></div></div>
    <div class="holder"><b>Lennart Vossberg</b><br><span>Geschäftsleitung</span></div>
    <div class="address">Ahornallee 42<br>44801 Bochum</div>
    <div class="divider"></div>
    <ul class="contact">
      <li><svg viewBox="0 0 10 10"><path d="M2 1l2 2-1 1.3a6 6 0 0 0 2.7 2.7L7 6l2 2-1.3 1.3C4 9 1 6 .7 2.3z" fill="currentColor"/></svg>+49 234-918273-0</li>
      <li><svg viewBox="0 0 10 10"><rect x="2.5" y="1" width="5" height="3" fill="none" stroke="currentColor"/><rect x="1" y="4" width="8" height="5" rx="1" fill="none" stroke="currentColor"/></svg>+49 234-918273-1</li>
      <li><svg viewBox="0 0 10 10"><rect x="1" y="2.5" width="8" height="5.5" fill="currentColor"/><path d="M1 2.5l4 3 4-3" stroke="#fff" fill="none"/></svg>info@vossberg-energie.de</li>
      <li><svg viewBox="0 0 10 10"><circle cx="5" cy="5" r="4" fill="none" stroke="currentColor"/><ellipse cx="5" cy="5" rx="1.8" ry="4" fill="none" stroke="currentColor"/><path d="M1 5h8" stroke="currentColor"/></svg>www.vossberg-energie.de</li>
    </ul>
    <div class="base-band"></div>
  </div>

  <div class="sheet card-back">
    <div class="wordmark"><i class="mark-square"></i><div class="name"><span>Energieberatung</span><span>Lennart Vossberg</span></div></div>
    <div class="url">www.vossberg-energie.de</div>
  </div>

  <div class="sheet variant variant-grey">
    <div class="wordmark"><i class="mark-square"></i><div class="name"><span>Energieberatung</span><span>Lennart Vossberg</span></div></div>
  </div>

  <div class="sheet variant variant-mono">
    <div class="wordmark"><i class="mark-square"></i><div class="name"><span>Energieberatung</span><span>Lennart Vossberg</span></div></div>
  </div>

  <div class="sheet letterhead">
    <div class="wordmark"><i class="mark-square"></i><div class="name"><span>Energieberatung</span><span>Lennart Vossberg</span></div></div>

    <div class="fold-mark" style="top:237px"></div>
    <div class="fold-mark" style="top:408px;width:28px"></div>
    <div class="fold-mark" style="top:530px"></div>

    <div class="sender-line">Energieberatung Lennart Vossberg - Postfach 1204 - 44801 Bochum</div>
    <div class="recipient">Firma Kettler und Partner<br>Herr Kettler<br>Lindenweg 18<br>44791 Bochum<br>Deutschland</div>

    <div class="letter-body">
      <p class="subject">Betreffzeile</p>
      <p class="salutation">Sehr geehrte Damen und Herren,</p>
      <p>schön, dass Sie neugierig reinschauen, obwohl hier ja eigentlich noch gar kein richtiger Text steht, sondern nur der sogenannte Blindtext. Dieser Blindtext will Ihnen nämlich sagen: Erstens will er den Texter entschuldigen – tut uns leid, aber es war einfach unmöglich, das Ding gestern Nacht noch exakt auf Länge runterzuschreiben. Das Briefing, Sie wissen schon. Schwieriges Thema. Und die Freundin ist krank, und der Freund wollte in diesen neuen Film. Und dann hat sich der Film so überhaupt nicht gelohnt, sagte er.</p>
      <p>Ja, und zweitens haben wir Sie bis hierhin zum Lesen gebracht und wollen damit belegen, dass nicht alle Marktforscher und Kaffeesatzleser recht haben, die sagen, dass unser armer Freund Otto Normalverbraucher und seine hässliche Schwester Lieschen Müller maximal Null Komma gar kein Interesse haben für Texte.</p>
      <p>Drittens sollten wir für ein paar Zeilen abschweifen und uns dem Gegenstand unserer Bemühungen zuwenden. Was heißt überhaupt Blindtext? Macht er blind, und wenn ja, wen? Ich denke, das Wörtchen will uns ja auch nur warnend darauf hinweisen, dass viel zu oft nach dem Motto „Augen zu und durch“ verfahren wird bei der verantwortungsvollen Aufgabe, Grauwert zu verteilen.</p>
      <p>Erstens will er den Texter entschuldigen – tut uns leid, aber es war einfach unmöglich, das Ding gestern Nacht noch exakt auf Länge runterzuschreiben. Das Briefing, Sie wissen schon. Schwieriges Thema. Und die Freundin ist krank, und der Freund wollte in diesen neuen Film. Und dann hat sich der Film so überhaupt nicht gelohnt, sagte er.</p>
      <p>Mit freundlichen Grüßen,</p>
      <p>Henrike Sallmann</p>
    </div>

    <footer class="letter-footer">
      <section><h4>Energieberatung Lennart Vossberg</h4>Ahornallee 42<br>44801 Bochum</section>
      <section><h4>Geschäftsführer</h4>Lennart Vossberg<br>Energieberater</section>
      <section>
        <ul class="contact">
          <li><svg viewBox="0 0 10 10"><path d="M2 1l2 2-1 1.3a6 6 0 0 0 2.7 2.7L7 6l2 2-1.3 1.3C4 9 1 6 .7 2.3z" fill="var(--teal)"/></svg>+49 234-918273-0</li>
          <li><svg viewBox="0 0 10 10"><rect x="2.5" y="1" width="5" height="3" fill="none" stroke="var(--teal)"/><rect x="1" y="4" width="8" height="5" rx="1" fill="none" stroke="var(--teal)"/></svg>+49 234-918273-1</li>
          <li><svg viewBox="0 0 10 10"><circle cx="5" cy="5" r="4" fill="none" stroke="var(--teal)"/><ellipse cx="5" cy="5" rx="1.8" ry="4" fill="none" stroke="var(--teal)"/><path d="M1 5h8" stroke="var(--teal)"/></svg>www.vossberg-energie.de</li>
        </ul>
      </section>
      <section><h4>Amtsgericht Stadt</h4>ABC 0000XX<br>UST-ID DE 000XX</section>
      <section><h4>Bankverbindung ABC</h4>IBAN DE12 3456 7890 1234 5678<br>BIC ABCDEF12345</section>
    </footer>

    <div class="base-band"></div>
  </div>

</div>
</body>
</html>
```